CBD Lotion package Design plus Box

Hi! We need a packaging design and a box for a CBD infused hand/ body lotion. Our company name is Tu Tu Fern and the product is called Marzelune. I think this will be our "flagship product" we are looking for a design that has a big Wow factor, it has to look modern, clean, and look like a premium brand. My 1st thought is a graffiti theme, but I'm open to any concept.

A. A few requirements-
1. No more then 2 colors (design)
2. The bottle & cap can be any color
3. No cannabis or hemp leaves please

B. Front of the bottle has to have the below items
Marzelune - Focus
Hemp Lotion
100% Natural
Tu Tu Fern logo - incorporated
250 MG CBD
7 oz
Fragrance: Jasmine Sambac

C. Back of the bottle has to have:

1.Attached QR code - Under the code can you please add or www.tutufern.com/lab-report

2. Bar code

----below is updated---4/4/19

Ingredients: Organic Aloe Leaf Juice, Organic Coconut Oil, Glycerin, Stearic Acid, Emulsifying Wax, Witch Hazel Water, Vitamin E, Sunflower Seed Oil, Phenoxyethanol, Organic Hemp Seed Oil, Rose Flower Water, Organic White Willow Bark Extract, Organic Rosemary Leaf Extract, Organic Neem Seed Oil, Organic Alcohol, Xanthan Gum, Tetrasodium Glutamate Diacetate

Directions: Apply to the hands & body as often as needed throughout the day to hydrate and nourish the skin.

Storage: Keep product in a cool dry play out of direct sunlight

84% Organic Content

Disclaimer: Consult your doctor before taking if you are pregnant or nursing, have a medical condition, or take pharmaceutical drugs. The statements made regarding these products have not been evaluated by the National Wellness Review Board. The efficacy of these products has not been confirmed by NWRB-approved research. These products are not intended to diagnose, treat, cure or prevent any disease. Warring- for external use only: do not get into eyes. Keep out of the reach of children.

5. Box same as the lotion back ( C) . The front (B) + logo or design concept from the bottle is fine

Target Market(s)

Millennials - Baby Boomers
Middle-Upper Income
Live in close Urben area (NYC, LA, ect)

Industry/Entity Type

Cosmetic

Colors

Designer to choose colors to be used in the design.

Requirements
Must have
• A. A few requirements-
• 1. No more then 2 colors (design)
• 2. The bottle & cap can be any color
• Front of the bottle has to have the below items
• Marzelune - main Focus
• Hemp Lotion -small
• 100% Natural - small
• Tu Tu Fern logo - 2nd emphasis
• 250 MG CBD
• 7 oz
• Fragrance: Jasmine Sambac
• ***Please see description
Nice to have
Should not have
• No cannabis or hemp leaves please

```html
<!DOCTYPE html>
<html lang="en">
<head>
<meta charset="utf-8">
<title>Tu Tu Fern – Marzelune Hemp Lotion</title>
<link rel="stylesheet" href="https://fonts.googleapis.com/css2?family=Open+Sans:wdth,wght@75..100,300..800&display=swap">
<style>
  :root {
    --backdrop: #000000;
    --label-top: #2e2e2e;
    --label-mid: #8a8378;
    --label-bottom: #e9b94a;
    --ink-light: #ffffff;
    --ink-gold: #c99a2e;
  }
  html, body {
    margin: 0;
    padding: 0;
    width: 1200px;
    height: 1200px;
    overflow: hidden;
    background: var(--backdrop);
  }
  .canvas {
    position: relative;
    width: 1200px;
    height: 1200px;
    background: var(--backdrop);
    font-family: "Open Sans", Arial, sans-serif;
  }
  .label {
    position: absolute;
    left: 380px;
    top: 60px;
    width: 440px;
    height: 1080px;
    background: linear-gradient(180deg, var(--label-top) 0%, #4a4a4a 30%, var(--label-mid) 52%, #c9a452 72%, var(--label-bottom) 100%);
    display: flex;
    flex-direction: column;
    align-items: center;
    color: var(--ink-light);
  }
  .brand {
    margin-top: 190px;
    display: flex;
    align-items: center;
    gap: 12px;
    font-weight: 600;
    font-stretch: 75%;
    font-size: 38px;
    letter-spacing: 0;
    line-height: 1;
  }
  .brand-mark {
    width: 18px;
    height: 18px;
    background: var(--ink-light);
  }
  .product-name {
    margin: 110px 0 0;
    font-weight: 700;
    font-size: 148px;
    line-height: 0.95;
    text-align: center;
    letter-spacing: 4px;
    text-transform: uppercase;
  }
  .product-name span { display: block; }
  .fragrance {
    margin-top: 36px;
    padding: 6px 22px;
    border-radius: 30px;
    background: var(--ink-light);
    color: var(--ink-gold);
    font-weight: 600;
    font-stretch: 75%;
    font-size: 30px;
    text-transform: uppercase;
  }
  .product-type {
    margin-top: 34px;
    font-weight: 400;
    font-stretch: 75%;
    font-size: 44px;
    text-transform: uppercase;
  }
  .specs {
    margin-top: 4px;
    text-align: center;
    font-stretch: 75%;
    text-transform: uppercase;
    line-height: 1.25;
  }
  .specs .natural { font-size: 24px; font-weight: 400; }
  .specs .dose, .specs .volume { font-size: 18px; font-weight: 600; }
</style>
</head>
<body>
<main class="canvas">
  <section class="label">
    <div class="brand"><span class="brand-mark"></span>Tu Tu Fern</div>
    <h1 class="product-name" aria-label="Marzelune">
      <span>Mar</span><span>zel</span><span>une</span>
    </h1>
    <div class="fragrance">Jasmine Sambac</div>
    <div class="product-type">Hemp Lotion</div>
    <div class="specs">
      <div class="natural">100% Natural</div>
      <div class="dose">250 mg CBD</div>
      <div class="volume">7 oz</div>
    </div>
  </section>
</main>
</body>
</html>
```